Quotation and Scripture Design

We are a marketing firm looking for a graphic designer who is gifted in the merging of typestyles, colors, and composition into images suitable for framing in the home or office. The design criteria is quite simple, (1) keep it fresh without looking dated or religious, and (2) push the envelope a little with good, solid graphic design. Phase one will involve building our inventory of original artwork to fifty or more pieces to be marketed online. For phase two in addition to a line of greeting cards, we will also offer art pieces reproduced by laser engravers, CNC routers, chemical etching, and digital printers. For this reason it is necessary that all art files be submitted in a vector format.

Target Market(s)

Professional women and men who appreciate and purchase gallery quality artwork.

Industry/Entity Type

Graphic Designer

Requirements
Must have
• Selection of the designer will be based on their graphic interruption of the following two quotations.
Quotation No. 1 - Romans 8:28
And we know that all things work together for good to those who love God, to those who are called according to His purpose.
Quotation No. 2 -Jeremiah 29:11
For I know the plans I have for you, declares the Lord. Plans to prosper you and not to harm you. Plans to give you hope and a future.
Design one of these two formats to fit a 8" x10" frame, and the other to fit a 12" x 12" frame.
Nice to have
• Rich colors, fresh typestyles . . . please no Times Roman. Bold, creative composition is what we are looking for.
Should not have
• Dated, religious artwork found in the local bible bookstore is a very good example of what we DO NOT want. If it is not something you would purchase for yourself or a friend, more than likely it won't meet our criteria.

```html
<!DOCTYPE html>
<html lang="en">
<head>
<meta charset="UTF-8">
<title>Jeremiah 29:11 – Plans for Hope</title>
<link rel="stylesheet" href="https://fonts.googleapis.com/css2?family=Dancing+Script:wght@500;600&family=Lora:ital@1&display=swap">
<style>
  :root {
    --ink: #ffffff;
    --shadow: rgba(40, 8, 8, 0.55);
    --sky: #d9d6d2;
    --leaf-deep: #8e1414;
    --leaf-bright: #c4281f;
    --leaf-warm: #d4442a;
    --grass: #6f7f3a;
    --grass-dark: #4e5c27;
    --path: #b9b4ad;
  }
  * { margin: 0; padding: 0; box-sizing: border-box; }
  html, body {
    width: 1200px;
    height: 1200px;
    overflow: hidden;
    background: var(--sky);
  }
  .artwork {
    position: relative;
    width: 1200px;
    height: 1200px;
    overflow: hidden;
  }
  .autumn-scene {
    position: absolute;
    inset: 0;
    background:
      radial-gradient(ellipse 520px 260px at 180px 1120px, var(--path) 0%, rgba(185,180,173,0) 70%),
      radial-gradient(ellipse 700px 320px at 900px 1150px, var(--grass) 0%, rgba(111,127,58,0) 75%),
      linear-gradient(180deg,
        var(--sky) 0%,
        var(--leaf-warm) 8%,
        var(--leaf-bright) 25%,
        var(--leaf-deep) 50%,
        var(--leaf-bright) 68%,
        #8a3a22 80%,
        var(--grass-dark) 92%,
        var(--grass) 100%);
  }
  .verse {
    position: absolute;
    inset: 0;
    padding-top: 66px;
    text-align: center;
    font-family: "Dancing Script", cursive;
    font-weight: 600;
    font-size: 112px;
    line-height: 130px;
    color: var(--ink);
    text-shadow: 3px 3px 6px var(--shadow);
    list-style: none;
  }
  .verse-line { display: block; white-space: nowrap; }
  .reference {
    position: absolute;
    right: 24px;
    bottom: 28px;
    font-family: "Lora", serif;
    font-style: italic;
    font-size: 42px;
    color: var(--ink);
    text-shadow: 2px 2px 4px var(--shadow);
  }
</style>
</head>
<body>
  <main class="artwork">
    <div class="autumn-scene" role="img" aria-label="Photograph of red autumn trees beside a curving path and green lawn"></div>
    <blockquote class="verse">
      <span class="verse-line">For I know the plans</span>
      <span class="verse-line">I have for you,</span>
      <span class="verse-line">declares the Lord.</span>
      <span class="verse-line">Plans to prosper</span>
      <span class="verse-line">you and not to harm you.</span>
      <span class="verse-line">Plans to give you</span>
      <span class="verse-line">hope and a future.</span>
    </blockquote>
    <cite class="reference">Jeremiah 29:11</cite>
  </main>
</body>
</html>
```